Clearstep Podiatry Care Advertisement Sandwich board

We need a Sandwich board design for our fungal nail clinic - please find attached the sandwich board dimensions.

The sandwich board itself will be displayed outside of a large health clinic and we need it to attract the attention of people walking by. We need a brochure holder included in the design which will hold our brochures which provides as clients with more information (please see attached also).

We are open to the designers creativity but we would like a similar theme portrayed on our board that is similar to our website (www.clearsteppodiatrycare.co.nz) and brochure that incorporates our logo which I have attached). The final design should communicate professionalism and be a minimalist look but modern to capture the attention of pedestrians.

Finally, we would like the website and phone number (07) 382 5164.

We look forward to seeing your work.

```html
<!DOCTYPE html>
<html lang="en">
<head>
<meta charset="utf-8">
<title>Clearstep Podiatry Care – Sandwich Board</title>
<link rel="stylesheet" href="https://fonts.googleapis.com/css2?family=Montserrat:wght@600;700;800&family=Oswald:wght@500&display=swap">
<style>
  :root {
    --backdrop: #3a3a3c;
    --blue-light: #4f7dc6;
    --blue-deep: #2d3a86;
    --blue-ring: #34469a;
    --white: #ffffff;
    --ink: #1b1b1f;
    --cyan-strip: #6ccdf2;
    --skin-warm: #f0c9ad;
    --skin-soft: #f7e0cf;
  }
  * { margin: 0; padding: 0; box-sizing: border-box; }
  html, body {
    width: 1200px; height: 694px; overflow: hidden;
    background: var(--backdrop);
  }
  .canvas { position: relative; width: 1200px; height: 694px; }
  .board {
    position: absolute; left: 339px; top: 17px;
    width: 688px; height: 871px;
    transform: scale(0.758); transform-origin: top left;
    background: var(--white);
  }
  .board-art { position: absolute; inset: 0; }
  .brochure-holder {
    position: absolute; left: 52px; top: 66px; width: 112px; height: 218px;
    background: var(--white);
    display: flex; align-items: center; justify-content: center;
    text-align: center;
    font-family: 'Oswald', sans-serif; font-weight: 500;
    font-size: 20px; line-height: 30px; color: var(--ink);
  }
  .brand-mark {
    position: absolute; left: 288px; top: 210px; width: 110px;
    text-align: center;
    font-family: 'Montserrat', sans-serif; font-weight: 700;
    font-size: 20px; color: var(--blue-deep);
  }
  .headline {
    position: absolute; left: 46px; top: 424px;
    font-family: 'Montserrat', sans-serif; font-weight: 700;
    font-size: 84px; line-height: 92px; letter-spacing: -1px;
    color: var(--white); white-space: nowrap;
  }
  .tagline {
    position: absolute; left: 45px; top: 616px; width: 602px; height: 42px;
    background: var(--white);
    display: flex; align-items: center; justify-content: center;
    font-family: 'Montserrat', sans-serif; font-weight: 600;
    font-size: 29px; letter-spacing: 4px; color: var(--ink);
    white-space: nowrap;
  }
  .phone {
    position: absolute; left: 44px; top: 664px;
    font-family: 'Montserrat', sans-serif; font-weight: 800;
    font-size: 84px; line-height: 96px; letter-spacing: -1px;
    color: var(--white); white-space: nowrap;
  }
  .website {
    position: absolute; left: 50px; top: 754px;
    font-family: 'Montserrat', sans-serif; font-weight: 700;
    font-size: 28px; letter-spacing: 1.6px;
    color: var(--white); white-space: nowrap;
  }
</style>
</head>
<body>
<div class="canvas">
  <div class="board">
    <svg class="board-art" width="688" height="871" viewBox="0 0 688 871">
      <defs>
        <linearGradient id="panelBlue" x1="0" y1="0" x2="1" y2="0.3">
          <stop offset="0" stop-color="var(--blue-light)"/>
          <stop offset="1" stop-color="var(--blue-deep)"/>
        </linearGradient>
        <radialGradient id="skinTone" cx="0.55" cy="0.45" r="0.5">
          <stop offset="0" stop-color="var(--skin-warm)"/>
          <stop offset="0.6" stop-color="var(--skin-soft)"/>
          <stop offset="1" stop-color="var(--white)"/>
        </radialGradient>
        <clipPath id="photoWindow">
          <path d="M393,0 L688,0 L688,356 C620,430 540,470 450,462 C330,450 240,360 246,250 C250,140 320,50 393,0 Z"/>
        </clipPath>
      </defs>
      <rect class="cyan-strip" x="32" y="820" width="623" height="51" fill="var(--cyan-strip)"/>
      <path class="blue-panel" d="M0,0 H688 V813 Q688,828 673,828 H15 Q0,828 0,813 Z" fill="url(#panelBlue)"/>
      <path class="photo-ring" d="M393,0 L688,0 L688,356 C620,430 540,470 450,462 C330,450 240,360 246,250 C250,140 320,50 393,0 Z" fill="none" stroke="var(--blue-ring)" stroke-width="26"/>
      <path class="photo-window" d="M393,0 L688,0 L688,356 C620,430 540,470 450,462 C330,450 240,360 246,250 C250,140 320,50 393,0 Z" fill="var(--white)"/>
      <g role="img" aria-label="Photo of bare feet standing on tiptoe" clip-path="url(#photoWindow)">
        <ellipse cx="500" cy="230" rx="230" ry="250" fill="url(#skinTone)"/>
      </g>
      <rect class="handle-slot" x="271" y="28" width="142" height="26" rx="13" fill="var(--white)"/>
      <circle class="brand-dot" cx="343" cy="170" r="30" fill="var(--white)" stroke="var(--blue-deep)" stroke-width="7"/>
    </svg>
    <div class="brochure-holder">BROCHURE<br>HOLDER</div>
    <div class="brand-mark">Clearstep</div>
    <h1 class="headline">Clearstep<br>Podiatry Care</h1>
    <p class="tagline">YOUR FUNGAL NAIL EXPERTS</p>
    <p class="phone">(07) 382 5164</p>
    <p class="website">www.clearsteppodiatrycare.co.nz</p>
  </div>
</div>
</body>
</html>
```